Innovative Strategic IT Solutions and Management Consulting

Looking for a fresh design idea to represent a company which specializes in innovative strategic IT solutions focusing on information assurance, enterprise content management, health information technology, web applications, strategic IT solutions and solutions architect.

KOVL...the company name means "new beginning" in Greek or the acronym for Keen-Option-Venture-Logic. We pride ourselves in understanding the client's business and needs before proposing an innovative solutions.

Innovation / Secure / Strategy - the core motto

Color: Maroon / Burgundy / Silver / White / Grey / Black

Primary focus color: Burgundy / Silver

```html
<!DOCTYPE html>
<html lang="en">
<head>
<meta charset="utf-8">
<title>KOVL — Innovative Strategic IT Solutions</title>
<link rel="stylesheet" href="https://fonts.googleapis.com/css2?family=Source+Sans+3:wght@300;400;600&display=swap">
<style>
:root{
  --maroon:#4f1017;
  --footer:#4e0f0a;
  --crimson:#8c0b0b;
  --button:#7d0505;
  --paper:#f1eff0;
  --ink:#2b2b2b;
  --muted:#444;
  --white:#ffffff;
  --rule:#4a4a4a;
}
*{margin:0;padding:0;box-sizing:border-box}
html,body{width:1093px;height:1200px;overflow:hidden}
body{font-family:"Source Sans 3",sans-serif;background:var(--white);color:var(--ink);position:relative}
.site-header{position:absolute;top:0;left:0;width:1093px;height:95px;background:var(--white)}
.brand{position:absolute;left:66px;top:24px;display:flex;align-items:center;gap:8px;font-size:38px;font-weight:600;color:var(--crimson);letter-spacing:1px}
.brand-dot{width:14px;height:14px;border-radius:50%;background:var(--crimson)}
.main-nav a{position:absolute;top:40px;font-size:12.5px;color:var(--ink);text-decoration:none;text-transform:uppercase}
.main-nav a.active::before{content:"";position:absolute;left:3px;right:3px;top:-8px;height:2px;background:#d9433a}
.hero{position:absolute;top:95px;left:0;width:1093px;height:503px;background:
  radial-gradient(ellipse at 30% 60%,#4a4a4a 0%,rgba(40,40,40,0) 60%),
  radial-gradient(ellipse at 75% 55%,#3c3c3c 0%,rgba(40,40,40,0) 55%),
  linear-gradient(180deg,#6b6b6b 0%,#565656 45%,#3a3a3a 100%);
  color:var(--white);text-align:center}
.hero h1{position:absolute;top:122px;left:0;width:100%;font-size:38px;font-weight:400;letter-spacing:.3px}
.hero h2{position:absolute;top:183px;left:0;width:100%;font-size:19px;font-weight:400}
.hero p{position:absolute;top:228px;left:334px;width:425px;font-size:14.5px;font-weight:300;line-height:19px}
.hero-cta{position:absolute;top:316px;left:485px;width:122px;height:50px;border:3px solid var(--white);color:var(--white);font-size:15px;font-weight:300;line-height:44px;text-decoration:none}
.hero-arrow{position:absolute;top:228px}
.service-band{position:absolute;top:598px;left:0;width:1093px;height:68px;background:var(--maroon);color:var(--white)}
.service-band span{position:absolute;top:23px;font-size:16.5px;display:flex;align-items:center;gap:10px}
.service-band svg{flex:none}
.features{position:absolute;top:666px;left:0;width:1093px;height:334px;background:var(--paper)}
.feature{position:absolute;top:34px;width:280px;text-align:center}
.feature svg{display:block;margin:0 auto}
.feature h3{margin-top:14px;font-size:19px;font-weight:400;color:var(--crimson)}
.feature p{margin:8px auto 0;font-size:11px;line-height:15px;color:var(--muted);width:250px}
.read-more{position:absolute;top:264px;width:120px;height:40px;background:var(--button);color:var(--white);font-size:17px;line-height:40px;text-align:center;text-decoration:none;box-shadow:3px 3px 4px rgba(0,0,0,.35)}
.site-footer{position:absolute;top:1000px;left:0;width:1093px;height:200px;background:var(--footer);border-top:4px solid var(--rule);color:var(--white)}
.footer-col{position:absolute;top:44px}
.footer-col h4{font-size:23px;font-weight:300;margin-bottom:14px}
.footer-col a,.footer-col p{display:block;font-size:14px;color:var(--white);text-decoration:none;line-height:26px}
.social{display:flex;gap:10px;margin-top:4px}
.social span{width:28px;height:28px;border:2px solid var(--white);border-radius:50%}
</style>
</head>
<body>
<header class="site-header">
  <div class="brand"><span>KOVL</span><span class="brand-dot"></span></div>
  <nav class="main-nav">
    <a class="active" href="#" style="left:559px">Home</a>
    <a href="#" style="left:638px">Solutions</a>
    <a href="#" style="left:746px">Strategy</a>
    <a href="#" style="left:846px">Security</a>
    <a href="#" style="left:942px">Technologies</a>
  </nav>
</header>

<section class="hero" role="img" aria-label="Blurred photo of business people meeting around a laptop in an office">
  <svg class="hero-arrow" style="left:66px" width="14" height="46" viewBox="0 0 14 46"><path d="M11 2 Q2 23 11 44" fill="none" stroke="#fff" stroke-width="3"/></svg>
  <h1>INNOVATIVE STRATEGIC IT SOLUTIONS</h1>
  <h2>Build/develop Custum website and Web Application</h2>
  <p>Web Development offers professional Website development services to help you successfully plan, create, maintain and market your Web development project.</p>
  <a class="hero-cta" href="#">LEARN MORE</a>
  <svg class="hero-arrow" style="left:1014px" width="14" height="46" viewBox="0 0 14 46"><path d="M3 2 Q12 23 3 44" fill="none" stroke="#fff" stroke-width="3"/></svg>
</section>

<nav class="service-band">
  <span style="left:66px"><svg width="18" height="18" viewBox="0 0 18 18"><rect x="1" y="4" width="12" height="12" rx="2" fill="#fff"/><path d="M8 10 L16 2" stroke="#fff" stroke-width="3"/></svg>Solutions Architect</span>
  <span style="left:324px"><svg width="16" height="18" viewBox="0 0 16 18"><rect x="1" y="2" width="14" height="15" fill="none" stroke="#fff" stroke-width="2"/><path d="M6 8 L4 10 L6 12 M10 8 L12 10 L10 12" stroke="#fff" fill="none"/></svg>Strategic Management</span>
  <span style="left:622px"><svg width="18" height="18" viewBox="0 0 18 18"><rect x="1" y="1" width="11" height="13" fill="none" stroke="#fff" stroke-width="2"/><circle cx="13" cy="13" r="4" fill="#fff"/></svg>Application Development</span>
  <span style="left:923px"><svg width="15" height="18" viewBox="0 0 15 18"><rect x="1" y="2" width="13" height="15" fill="#fff"/><path d="M7.5 6 V13 M4 9.5 H11" stroke="#4f1017" stroke-width="2"/></svg>Health IT</span>
</nav>

<section class="features">
  <div class="feature" style="left:67px">
    <svg width="96" height="96" viewBox="0 0 96 96"><circle cx="48" cy="48" r="44" fill="#fff" stroke="#111" stroke-width="5"/><rect x="22" y="30" width="52" height="34" fill="none" stroke="#111" stroke-width="5"/><path d="M42 64 V72 M54 64 V72 M36 73 H60" stroke="#111" stroke-width="4"/><path d="M40 56 L62 26" stroke="#111" stroke-width="5"/></svg>
    <h3>Innovative Solutions</h3>
    <p>We create meaningful websites that offer simplistic user experiences, achieve high rankings on the most popular search engines and promote your brand to the widest possible audience.</p>
  </div>
  <a class="read-more" href="#" style="left:147px">Read More</a>

  <div class="feature" style="left:402px">
    <svg width="96" height="96" viewBox="0 0 96 96"><circle cx="48" cy="48" r="44" fill="#fff" stroke="#111" stroke-width="5"/><rect x="36" y="18" width="24" height="10" fill="#111"/><rect x="30" y="30" width="36" height="46" rx="4" fill="none" stroke="#111" stroke-width="5"/><path d="M48 42 V64 M37 53 H59" stroke="#111" stroke-width="7"/></svg>
    <h3>Health IT</h3>
    <p>Our emphasis on quality code and our straight-forward approach to custom web solutions will streamline your operations. We focus on scalable development to ensure pain-free maintenance and application longevity.</p>
  </div>
  <a class="read-more" href="#" style="left:481px">Read More</a>

  <div class="feature" style="left:750px">
    <svg width="96" height="96" viewBox="0 0 96 96"><circle cx="48" cy="48" r="44" fill="#fff" stroke="#111" stroke-width="5"/><path d="M30 44 L48 28 L66 44 V60 H30 Z" fill="#111"/><rect x="44" y="48" width="8" height="12" fill="#fff"/><path d="M22 66 Q40 60 52 66 L74 60" fill="none" stroke="#111" stroke-width="5"/></svg>
    <h3>Information Assurance</h3>
    <p>Our Internet marketing and content experts work closely with clients to maximize their online presence. Obtain top rankings for desired search terms and drive qualified leads that are crucial to building your business and brand.</p>
  </div>
  <a class="read-more" href="#" style="left:831px">Read More</a>
</section>

<footer class="site-footer">
  <div class="footer-col" style="left:66px"><h4>Services</h4><a href="#">Solutions Architect</a><a href="#">Strategic Management</a><a href="#">Application Development</a><a href="#">Health IT</a></div>
  <div class="footer-col" style="left:266px"><h4>About Us</h4><a href="#">Company Profile</a><a href="#">Our Team</a><a href="#">Company Culture</a></div>
  <div class="footer-col" style="left:474px"><h4>Stay Connected</h4><div class="social" aria-label="Social links"><span></span><span></span><span></span><span></span></div></div>
  <div class="footer-col" style="left:754px"><h4>Blog</h4><a href="#">Construct An</a><a href="#">IT Solution.</a></div>
  <div class="footer-col" style="left:925px"><h4>Legal Stuff</h4><p style="line-height:19px">© 2014 KOVL<br>IT solutions . All<br>Rights Reserved</p></div>
</footer>
</body>
</html>
```